Visitenkarten-Design für Gesundheits- und Ernährungsberaterin
Zielgruppe
Ich bin Gesundheit und Ernährungsberaterin
Zielgruppe sind chronisch Kranke und Gesundheitsbewusste Personen
Aufgabenstellung
Schlichtes aber direkt erkennbares Design.
Mahl mit Maß , Gesundheit und Ernährungsberatung ( gut lesbar , elegant)
Marlene Obruk-Feistinger ( nicht so groß )
Grau ; Grün Töne und gerne etwas rosa
Infos wie Adresse und E-Mail vielleicht in jeweilige Blöcke am unteren Rand

```html
<!DOCTYPE html>
<html lang="de">
<head>
<meta charset="utf-8">
<title>Visitenkarte – Mahl mit Maß</title>
<link rel="stylesheet" href="https://fonts.googleapis.com/css2?family=Arimo:wght@400&display=swap">
<style>
  :root {
    --stage: #4b4b4c;
    --card: #ffffff;
    --green: #7c9f6b;
    --green-dark: #5f8250;
    --rose: #d97c92;
    --band: #d6d6d6;
    --subtitle: #8f8f8f;
    --on-green: #ffffff;
  }
  * { box-sizing: border-box; margin: 0; padding: 0; }
  html, body {
    width: 1200px; height: 1200px; overflow: hidden;
    background: var(--stage);
    font-family: "Arimo", Arial, sans-serif;
  }
  .card {
    position: absolute; left: 50px; top: 295px;
    width: 1100px; height: 611px;
    background: var(--card);
    overflow: hidden;
  }
  .card__waves { position: absolute; inset: 0; width: 100%; height: 100%; }
  .portrait {
    position: absolute; left: 119px; top: 94px;
    width: 202px; height: 202px; border-radius: 50%;
    background: radial-gradient(circle at 52% 60%, #b7cf98 0 14%, #e6e8e2 34%, #f4f4f4 60%, #e4e4e6 100%);
  }
  .identity { position: absolute; left: 396px; top: 132px; }
  .identity__brand {
    font-size: 34px; color: var(--green-dark); font-weight: 400; line-height: 1.15;
  }
  .identity__name {
    margin-top: 10px;
    font-size: 26px; color: var(--rose); font-weight: 400; line-height: 1.15;
  }
  .identity__role {
    margin-top: 6px; font-size: 20px; color: var(--subtitle); line-height: 1.2;
  }
  .contact {
    position: absolute; color: var(--on-green);
    font-size: 26px; line-height: 31px;
    transform: translateY(-50%);
    white-space: nowrap;
  }
  .contact__icon {
    position: absolute; width: 28px; height: 28px; fill: var(--on-green);
    left: -48px; top: 50%; transform: translateY(-50%);
  }
  .contact--address { left: 233px; top: 435px; }
  .contact--phone { left: 233px; top: 491px; }
  .contact--mobile { left: 610px; top: 448px; }
  .contact--mail { left: 610px; top: 491px; }
</style>
</head>
<body>
  <div class="card">
    <svg class="card__waves" viewBox="0 0 1332 740" preserveAspectRatio="none" aria-hidden="true">
      <path d="M0 339 C 300 460, 800 470, 1332 260 L1332 740 L0 740 Z" fill="var(--band)"/>
      <path d="M0 362 C 300 483, 800 493, 1332 282 L1332 740 L0 740 Z" fill="var(--green)"/>
    </svg>

    <div class="portrait" role="img" aria-label="Foto: Beraterin im weißen Kittel hält frisches Obst und Gemüse"></div>

    <div class="identity">
      <p class="identity__brand">Mahl mit Maß</p>
      <h1 class="identity__name">Marlene Obruk-Feistinger</h1>
      <p class="identity__role">Gesundheit und Ernährungsberaterin</p>
    </div>

    <div class="contact contact--address">
      <svg class="contact__icon" viewBox="0 0 24 24" aria-hidden="true"><path d="M12 2a7 7 0 0 0-7 7c0 5 7 13 7 13s7-8 7-13a7 7 0 0 0-7-7zm0 9.5A2.5 2.5 0 1 1 12 6.5a2.5 2.5 0 0 1 0 5z"/></svg>
      <span>Lindenhufe 7,<br>24619 Bornhöved</span>
    </div>

    <div class="contact contact--phone">
      <svg class="contact__icon" viewBox="0 0 24 24" aria-hidden="true"><path d="M6.6 10.8a15 15 0 0 0 6.6 6.6l2.2-2.2a1 1 0 0 1 1-.25 11.4 11.4 0 0 0 3.6.57 1 1 0 0 1 1 1V20a1 1 0 0 1-1 1A17 17 0 0 1 3 4a1 1 0 0 1 1-1h3.5a1 1 0 0 1 1 1c0 1.250.2 2.45.57 3.57a1 1 0 0 1-.25 1z"/></svg>
      <span>04323/5827146</span>
    </div>

    <div class="contact contact--mobile">
      <svg class="contact__icon" viewBox="0 0 24 24" aria-hidden="true"><path d="M8 2h8a1.5 1.5 0 0 1 1.5 1.5v17A1.5 1.5 0 0 1 16 22H8a1.5 1.5 0 0 1-1.5-1.5v-17A1.5 1.5 0 0 1 8 2zm0 3v12.5h8V5zm4 14a1 1 0 1 0 0 2 1 1 0 0 0 0-2z"/></svg>
      <span>0152/73049186</span>
    </div>

    <div class="contact contact--mail">
      <svg class="contact__icon" viewBox="0 0 24 24" aria-hidden="true"><path d="M2 6h20v1.2l-10 6.3L2 7.2zm0 3.4 7 4.4-7 5zm20 0v9.4l-7-5zM10.6 14.7l1.4.9 1.4-.9L21.5 20h-19z"/></svg>
      <span>ernaehrung-mof@postkasten.de</span>
    </div>
  </div>
</body>
</html>
```